Presentation and Communication Coaching Services Business needs updated interactive web site

I want to keep the color scheme, functionality, and pages of my current site, but with a newer/updated look. I need to improve security and simplify images, etc. (Please see current site http://brackwellvoicetutor.com ) This will need be functional on mobile devices, as well.

I'm attached to the scrolling client list and scrolling client feedback.

Industry/Entity Type

Professional Service

Font styles to use
Sans Serif

Colors
0356a4
f37122
33a6d7

Requirements
Must have
• scrolling client banner on home page, client comments slider, color scheme
• Please see current site: http://brackwellvoicetutor.com
Nice to have
• better action/appearance
Should not have
• I don't want it to look like all the other sites/templates

```html
<!DOCTYPE html>
<html lang="en">
<head>
<meta charset="utf-8">
<title>Brackwell Voice Consulting</title>
<link href="https://fonts.googleapis.com/css2?family=Lato:wght@400;700&family=Open+Sans:wght@400;600;700&family=Roboto+Condensed:wght@400;700&display=swap" rel="stylesheet">
<style>
:root{
  --navy:#0356a4;
  --orange:#f37122;
  --sky:#33a6d7;
  --ink:#222;
  --muted:#555;
  --dark:#111418;
  --hero:#23262c;
}
*{box-sizing:border-box;margin:0;padding:0}
html,body{width:1200px;height:4932px;overflow:hidden}
body{position:relative;background:#fff;font-family:"Open Sans",sans-serif;color:var(--ink)}
.abs{position:absolute}
.heading{font-family:"Roboto Condensed",sans-serif;font-weight:400;text-align:center;width:1200px;left:0}

/* header + hero */
.hero{top:0;left:0;width:1200px;height:830px;background:linear-gradient(160deg,#3a3d44 0%,var(--hero) 55%,#15171b 100%)}
.hero-cut{top:560px;left:0}
.topbar{top:22px;left:170px;width:880px;height:30px;display:flex;align-items:center;justify-content:space-between;color:#fff;font-size:15px}
.topbar .phone{display:flex;align-items:center;gap:8px}
.brand{font-family:"Lato",sans-serif;font-size:24px;color:#fff;letter-spacing:.3px}
.login{background:var(--orange);color:#fff;border-radius:16px;padding:6px 16px;font-size:14px}
.nav{top:72px;left:150px;width:900px;border-bottom:1px solid rgba(255,255,255,.35);display:flex;justify-content:space-between;padding:0 14px 8px;font-size:15px;color:#fff}
.nav .active{color:var(--sky)}
.arrow{top:270px;color:#fff;font-size:22px}
.hero-name{top:200px;left:0;width:1200px;text-align:center;font-family:"Lato",sans-serif;font-size:72px;font-weight:400}
.hero-name .first{color:var(--sky)}
.hero-name .last{color:var(--orange)}
.hero-role{top:295px;left:0;width:1200px;text-align:center;font-family:"Lato",sans-serif;font-size:38px;color:#fff}
.video{top:428px;left:247px;width:708px;height:397px;background:#1c3f64;padding:14px}
.video-shot{width:100%;height:100%;background:linear-gradient(120deg,#7a5a48,#b08670 45%,#5b4536)}
.play{top:148px;left:314px}

/* offerings */
.offer-title{top:895px;font-size:40px;color:#111}
.offer-list{top:995px;list-style:none;font-size:15px;color:#333}
.offer-list li{display:flex;align-items:center;gap:10px;height:34px}
.dot{width:13px;height:13px;border-radius:50%;background:var(--orange);flex:none;position:relative}
.dot::after{content:"";position:absolute;left:3px;top:3px;width:5px;height:3px;border-left:2px solid #fff;border-bottom:2px solid #fff;transform:rotate(-45deg)}

/* band */
.band{top:1240px;left:0}
.band-photo-frame{top:1414px;left:132px;width:460px;height:314px;border:3px solid #fff}
.band-photo{top:1434px;left:160px;width:430px;height:300px;background:linear-gradient(110deg,#e9e6e2 0%,#c9c3bd 45%,#3b3e44 100%)}
.band-text{top:1440px;left:618px;width:470px;color:#fff}
.band-text h3{font-family:"Lato",sans-serif;font-weight:400;font-size:34px;line-height:42px;margin-bottom:14px;white-space:nowrap}
.band-text p{font-size:14px;line-height:24px;width:440px}

/* services */
.services-title{top:1930px;font-size:40px;color:#111}
.card{width:432px;height:192px;border:2px solid var(--navy);border-radius:4px;padding:28px 20px 0 140px;background:#fff}
.card.lead{background:var(--sky);border-color:var(--sky);color:#fff}
.card .icon{position:absolute;left:28px;top:28px;width:88px;height:88px;border-radius:50%;background:var(--navy);display:flex;align-items:center;justify-content:center}
.card.lead .icon{background:#fff}
.card h4{font-family:"Lato",sans-serif;font-size:19px;font-weight:700;letter-spacing:.3px;white-space:nowrap}
.card .rule{width:40px;height:2px;background:var(--orange);margin:6px 0 14px}
.card.lead .rule{background:#fff}
.card p{font-size:14px;line-height:21px;color:#444}
.card.lead p{color:#fff}

/* reviews */
.reviews{top:2630px;left:0}
.reviews-title{top:2722px;font-size:40px;color:#fff}
.review-photo{top:2796px;left:200px;width:236px;height:236px;border-radius:50%;border:6px solid #3a6fb2;background:linear-gradient(160deg,#c7a98f,#7c5e4a)}
.review-text{top:2820px;left:460px;width:560px;color:#fff;font-size:15px;line-height:31px}
.review-text .by{display:block;font-style:italic;margin-top:4px}
.chev{top:2872px}

/* publications */
.pubs-title{top:3276px;font-size:40px;color:#111}
.pub{top:3382px;height:310px}
.pub .cover{width:100%;height:100%}
.pub .caption{position:absolute;top:328px;left:-40px;right:-40px;text-align:center;font-size:16px;color:#222}

/* clients */
.clients-bg{top:3790px;left:0}
.clients-title{top:3980px;font-size:40px;color:#111}
.logo{width:210px;height:100px;background:#fff;border-radius:3px;box-shadow:0 2px 8px rgba(0,0,0,.12);display:flex;align-items:center;justify-content:center;gap:8px;font-family:"Open Sans",sans-serif;font-weight:600;font-size:22px;color:var(--navy)}

/* footer */
.footer{top:4440px;left:0}
.foot-col{top:4598px;color:#fff;font-size:14px}
.foot-col h5{font-family:"Lato",sans-serif;font-weight:400;font-size:16px;letter-spacing:.5px;margin-bottom:22px}
.foot-col li{list-style:none;line-height:25px;font-size:14px;color:#ddd}
.contact-item{display:flex;gap:10px;margin-bottom:18px}
.contact-item b{display:block;font-weight:400;font-size:14px;color:#fff}
.contact-item span{font-size:13px;color:#ccc}
.field{width:262px;height:28px;background:#fff;margin-top:10px;font-size:13px;color:#777;padding:5px 10px}
.btn{display:inline-block;margin-top:12px;background:var(--navy);color:#fff;font-size:14px;padding:6px 12px}
.foot-rule{top:4850px;left:158px;width:888px;height:1px;background:#3a3d42}
.copyright{top:4878px;left:0;width:1200px;text-align:center;font-size:13px;color:#ccc}
</style>
</head>
<body>

<div class="abs hero" role="img" aria-label="Dark photo of a speaker addressing an audience"></div>
<svg class="abs hero-cut" width="1200" height="280" viewBox="0 0 1200 280"><polygon points="0,270 1200,0 1200,280 0,280" fill="#fff"/></svg>

<div class="abs topbar">
  <div class="phone"><svg width="14" height="14" viewBox="0 0 24 24"><path d="M6.6 10.8a15 15 0 006.6 6.6l2.2-2.2c.3-.3.7-.4 1-.2 1.1.4 2.3.6 3.6.6.6 0 1 .4 1 1V20c0 .6-.4 1-1 1C10.6 21 3 13.4 3 4c0-.6.4-1 1-1h3.5c.6 0 1 .4 1 1 0 1.3.2 2.5.6 3.6.1.3 0 .7-.2 1z" fill="#33a6d7"/></svg>+1 555-014-2287</div>
  <div class="brand">Brackwell Voice Consulting</div>
  <div class="login">Client login</div>
</div>
<div class="abs nav">
  <span class="active">Home</span><span>About</span><span>Clients</span><span>Reviews</span><span>Services</span><span>Contact</span><span>Speaking Secrets</span>
</div>
<div class="abs arrow" style="left:100px">&#8249;</div>
<div class="abs arrow" style="left:1100px">&#8250;</div>
<div class="abs hero-name"><span class="first">Danielle</span> <span class="last">Brackwell</span></div>
<div class="abs hero-role">Public Speaking Consultant</div>
<div class="abs video">
  <div class="video-shot" role="img" aria-label="Video still of the consultant standing in a living room"></div>
  <svg class="abs play" width="80" height="80" viewBox="0 0 80 80"><circle cx="40" cy="40" r="36" fill="rgba(255,255,255,.9)"/><polygon points="32,24 58,40 32,56" fill="#333"/></svg>
</div>

<h2 class="abs heading offer-title">BVC Provides Training, Tools, and Techniques</h2>
<ul class="abs offer-list" style="left:158px">
  <li><span class="dot"></span>Executive Presence – Polishing Personal Presentation/Manner</li>
  <li><span class="dot"></span>Addressing and Overcoming Speaking/Communication Anxiety</li>
  <li><span class="dot"></span>Last-Minute Presentation 911</li>
  <li><span class="dot"></span>Media Training</li>
  <li><span class="dot"></span>Modifying Accents for Clarity and Intelligibility</li>
  <li><span class="dot"></span>Communicating Complex/Technical Material to Any Audience</li>
</ul>
<ul class="abs offer-list" style="left:707px">
  <li><span class="dot"></span>Cultivating a More Effective Communication Style</li>
  <li><span class="dot"></span>Incorporating and Interacting with Audio/Visual Aids</li>
  <li><span class="dot"></span>Developing Tools for Dynamic Speaking</li>
  <li><span class="dot"></span>Conducting Communication 360° Interviews</li>
  <li><span class="dot"></span>Sharpening Presentation Skills for Attorneys</li>
</ul>

<svg class="abs band" width="1200" height="560" viewBox="0 0 1200 560">
  <defs><linearGradient id="bandGrad" x1="0" y1="0" x2="1" y2="1"><stop offset="0" stop-color="#0a2f86"/><stop offset=".6" stop-color="#0356a4"/><stop offset="1" stop-color="#0b3d9a"/></linearGradient></defs>
  <polygon points="0,90 1200,0 1200,560 0,560" fill="url(#bandGrad)"/>
</svg>
<div class="abs band-photo-frame"></div>
<div class="abs band-photo" role="img" aria-label="Photo of a smiling businesswoman with arms crossed in an office"></div>
<div class="abs band-text">
  <h3>You're good at what you do.<br>Learn How to let it show.</h3>
  <p>An individual works hard to reach a place of respect and authority in her or his chosen profession. Effective self-presentation adds confidence and allows one's unique personality and expertise to shine through – in fact, it is key in separating from the pack and reaching higher goals. As competition increases, these skills become more essential in demonstrating value to an employer, manager, or board.</p>
</div>

<h2 class="abs heading services-title">Our Services</h2>
<div class="abs card lead" style="top:2056px;left:158px">
  <div class="icon"><svg width="40" height="40" viewBox="0 0 24 24"><rect x="2" y="3" width="20" height="13" rx="1" fill="none" stroke="#0356a4" stroke-width="2"/><path d="M8 21h8M12 16v5" stroke="#0356a4" stroke-width="2"/></svg></div>
  <h4>01. COACHING</h4><div class="rule"></div>
  <p>One-on-one, individual, and customized to your unique goals, obstacles, and challenges.</p>
</div>
<div class="abs card" style="top:2056px;left:614px">
  <div class="icon"><svg width="40" height="40" viewBox="0 0 24 24"><path d="M12 2a7 7 0 00-4 12.7V18h8v-3.3A7 7 0 0012 2z" fill="none" stroke="#fff" stroke-width="2"/><path d="M9 21h6" stroke="#fff" stroke-width="2"/></svg></div>
  <h4>03. Accents</h4><div class="rule"></div>
  <p>Support for executives from outside the U.S. to increase intelligibility and diminish obstacles to successful communication in</p>
</div>
<div class="abs card" style="top:2286px;left:158px">
  <div class="icon"><svg width="44" height="44" viewBox="0 0 24 24"><circle cx="9" cy="12" r="3.5" fill="none" stroke="#fff" stroke-width="2.4" stroke-dasharray="2 1.4"/><circle cx="17" cy="7" r="2.5" fill="none" stroke="#fff" stroke-width="2" stroke-dasharray="1.6 1.2"/><circle cx="17" cy="17" r="2.5" fill="none" stroke="#fff" stroke-width="2" stroke-dasharray="1.6 1.2"/></svg></div>
  <h4>02. CUSTOM WORKSHOPS</h4><div class="rule"></div>
  <p>Unique, effective program design and facilitation to match the needs of executives, managers, or promoting</p>
</div>
<div class="abs card" style="top:2286px;left:614px">
  <div class="icon"><svg width="38" height="38" viewBox="0 0 24 24"><path d="M5 2h9l5 5v15H5z" fill="#fff"/><path d="M14 2v5h5" fill="#cfe0f2"/></svg></div>
  <h4>04. Keynote Speeches</h4><div class="rule"></div>
  <p>Fresh ways of thinking about speaking and communication combined with practical tools for participants of your</p>
</div>

<svg class="abs reviews" width="1200" height="560" viewBox="0 0 1200 560">
  <defs><linearGradient id="revGrad" x1="0" y1="0" x2="0" y2="1"><stop offset="0" stop-color="#e8681c"/><stop offset=".55" stop-color="#f37122"/><stop offset="1" stop-color="#d45a14"/></linearGradient></defs>
  <rect width="1200" height="560" fill="url(#revGrad)"/>
  <polygon points="0,460 1200,560 0,560" fill="#fff"/>
</svg>
<h2 class="abs heading reviews-title">Reviews</h2>
<svg class="abs chev" style="left:100px" width="36" height="70" viewBox="0 0 36 70"><path d="M32 4L6 35l26 31" fill="none" stroke="#fff" stroke-width="3"/></svg>
<svg class="abs chev" style="left:1064px" width="36" height="70" viewBox="0 0 36 70"><path d="M4 4l26 31L4 66" fill="none" stroke="#fff" stroke-width="3"/></svg>
<div class="abs review-photo" role="img" aria-label="Portrait photo of a client"></div>
<div class="abs review-text">" It is a long established fact that a reader will be distracted by the readable content of a page when looking at its layout. The point of using Lorem Ipsum is that it has a more-or-less normal distribution of letters, as opposed to using 'Content here, content here', making it look like readable English. Many desktop publishing packages and web page editors now use Lorem Ipsum as their default model text "<span class="by">- ERIC, CLIENT AT NORVANE MICRO USA</span></div>

<h2 class="abs heading pubs-title">Recent Publications</h2>
<div class="abs pub" style="left:181px;width:240px"><div class="cover" role="img" aria-label="Magazine cover featuring a woman" style="background:linear-gradient(160deg,#5fb4d8,#2c7fb0 50%,#c9a882)"></div><div class="caption">Lumen Weekly Magazine</div></div>
<div class="abs pub" style="left:460px;width:226px"><div class="cover" role="img" aria-label="Newspaper photo of a man at microphones" style="background:linear-gradient(180deg,#7a1a14,#3a0e0c 60%,#1a1a1a)"></div><div class="caption">Harbor City Post</div></div>
<div class="abs pub" style="left:778px;width:242px"><div class="cover" role="img" aria-label="Magazine cover in blue and yellow" style="background:linear-gradient(170deg,#2a62b8,#1b3f86 60%,#e0b52a)"></div><div class="caption">Summer Gentry Style Annual</div></div>

<svg class="abs clients-bg" width="1200" height="670" viewBox="0 0 1200 670">
  <polygon points="0,110 1200,0 1200,670 0,670" fill="#efefef"/>
</svg>
<h2 class="abs heading clients-title">Client</h2>
<div class="abs logo" style="top:4106px;left:141px">Pellam</div>
<div class="abs logo" style="top:4106px;left:372px">Nimbus Group</div>
<div class="abs logo" style="top:4106px;left:605px">Tarvine</div>
<div class="abs logo" style="top:4106px;left:836px">Halberd</div>
<div class="abs logo" style="top:4244px;left:141px">Quillory</div>
<div class="abs logo" style="top:4244px;left:372px">Brightlane</div>
<div class="abs logo" style="top:4244px;left:605px">Westhaven</div>
<div class="abs logo" style="top:4244px;left:836px">Kestrel Group</div>

<svg class="abs footer" width="1200" height="492" viewBox="0 0 1200 492">
  <polygon points="0,90 1200,0 1200,492 0,492" fill="#111418"/>
</svg>
<div class="abs foot-col" style="left:158px">
  <h5>CONTACT US</h5>
  <div class="contact-item"><svg width="16" height="14" viewBox="0 0 24 20"><rect x="1" y="1" width="22" height="18" fill="none" stroke="#fff" stroke-width="2"/><path d="M1 2l11 9 11-9" fill="none" stroke="#fff" stroke-width="2"/></svg><div><b>EMAIL ADDRESS</b><span>info@brackwellvoicetutor.com</span></div></div>
  <div class="contact-item"><svg width="16" height="16" viewBox="0 0 24 24"><path d="M6.6 10.8a15 15 0 006.6 6.6l2.2-2.2c.3-.3.7-.4 1-.2 1.1.4 2.3.6 3.6.6.6 0 1 .4 1 1V20c0 .6-.4 1-1 1C10.6 21 3 13.4 3 4c0-.6.4-1 1-1h3.5c.6 0 1 .4 1 1 0 1.3.2 2.5.6 3.6.1.3 0 .7-.2 1z" fill="#fff"/></svg><div><b>PHONE NUMBER</b><span>555.013.4471</span></div></div>
</div>
<div class="abs foot-col" style="left:444px">
  <h5>LINKS</h5>
  <ul><li>Home</li><li>About Us</li><li>Support Center</li><li>Services</li></ul>
</div>
<div class="abs foot-col" style="left:592px">
  <h5>RESOURCES</h5>
  <ul><li>Reviews</li><li>Services</li><li>Speaking Secrets</li><li>Contact Us</li></ul>
</div>
<div class="abs foot-col" style="left:780px">
  <h5 style="margin-bottom:4px">REGISTER AND RECEIVE FREE</h5>
  <div style="font-size:12px;color:#ddd">"5 HABITS OF CLEAR SPEAKERS"</div>
  <div class="field">Your Name</div>
  <div class="field">Email address</div>
  <div class="btn">Register Now !</div>
</div>
<div class="abs foot-rule"></div>
<div class="abs copyright">© Copyright 2018 . All Rights Reserved. Terms and Conditions | Privacy Policy</div>

</body>
</html>
```